Maple Crest Home Health Care of San Diego needs a brochure to advertise its services.

We need a brochure for a new company called Maple Crest Home Health Care of San Diego, Inc. We provide skilled home health care services such as skilled nursing, physical, occupational, and speech therapy, medical social work, and home health aide services. Our patient population is mostly 65 years and older. We market our services in the community, including hospitals, skilled nursing and assisted living facilities, doctor's offices etc. We would like to see designs that are easy to read, go with our logo color, which is green, and includes pictures of multicultural elderly individuals receiving medical or rehab care in or surrounding the home. Please include the information contained in the files attached, which has our services, about home health care, and our mission and vision.
Maple Crest Home Health Care of San Diego, Inc.
4827 Harbor Glen Road, Suite 3K
Encinitas, CA 92031
760-418-MAPL (office)
76- 529-MAPL (fax)
760-284-5536 (cell)

Target Market(s)

See above

Industry/Entity Type

Home Health Care

Font styles to use
Sans Serif

Colors
9bcb3c
add136

Requirements
Must have
• Must be tri-fold and geared toward an elderly and medical field population. Please view some other home health agency brochures out there for examples.

```html
<!DOCTYPE html>
<html lang="en">
<head>
<meta charset="utf-8">
<title>Maple Crest Home Health Care – Tri-fold Brochure</title>
<link rel="stylesheet" href="https://fonts.googleapis.com/css2?family=Open+Sans:wght@400;600;700;800&display=swap">
<style>
  :root {
    --green: #0f9a48;
    --green-dark: #0b7f3b;
    --lime: #9bcb3c;
    --lime-light: #add136;
    --ink: #1f1f1f;
    --paper: #ffffff;
    --backdrop: #e4e4e4;
  }
  * { box-sizing: border-box; margin: 0; padding: 0; }
  html, body { width: 1200px; height: 919px; overflow: hidden; }
  body {
    background: var(--backdrop);
    font-family: "Open Sans", Arial, sans-serif;
    color: var(--ink);
    position: relative;
  }
  .brochure {
    position: absolute; left: 45px; top: 30px;
    width: 1110px; height: 858px;
    background: var(--paper);
    overflow: hidden;
    box-shadow: 0 6px 24px rgba(0,0,0,.18);
  }
  .wave { position: absolute; left: 0; top: 0; width: 1110px; height: 858px; }
  .panel { position: absolute; top: 0; width: 370px; height: 858px; }
  .panel--about { left: 0; }
  .panel--contact { left: 370px; }
  .panel--cover { left: 740px; }
  .fold {
    position: absolute; top: 0; width: 1px; height: 858px;
    background: rgba(0,0,0,.06);
  }

  /* About panel */
  .about__title {
    position: absolute; left: 40px; top: 38px; width: 290px;
    text-align: center; color: var(--green);
    font-size: 21px; font-weight: 700; line-height: 1.25;
  }
  .about__body {
    position: absolute; left: 36px; top: 104px; width: 298px;
    font-size: 13px; line-height: 1.38; text-align: justify;
  }
  .about__body p + p { margin-top: 10px; }
  .about__body strong { font-weight: 700; }
  .about__photo {
    position: absolute; left: 66px; top: 484px;
    width: 118px; height: 118px; border-radius: 50%;
    background: radial-gradient(circle at 45% 45%, #e9c3a6, #c98e6c 60%, #f3ede6);
    border: 5px solid var(--lime);
  }
  .quote {
    position: absolute; left: 40px; top: 660px; width: 300px;
    color: #fff; font-size: 25px; font-weight: 700; line-height: 1.55;
  }
  .quote__mark { color: var(--lime-light); font-size: 34px; line-height: 0; }

  /* Contact panel */
  .contact__photo {
    position: absolute; left: 28px; top: 28px; width: 314px; height: 236px;
    border-radius: 20px;
    background: linear-gradient(135deg, #d9c59c 0%, #b58b5a 45%, #6c7fb0 100%);
  }
  .notice {
    position: absolute; left: 34px; top: 292px; width: 302px;
    color: var(--green); font-size: 14px; line-height: 1.45; text-align: center;
  }
  .brand {
    display: flex; align-items: center; gap: 10px;
    color: var(--green); font-weight: 700;
  }
  .brand__dot { width: 34px; height: 34px; border-radius: 50%; background: var(--lime); flex: none; }
  .brand--small {
    position: absolute; left: 50px; top: 500px; width: 270px;
    justify-content: center; font-size: 14px; line-height: 1.2;
  }
  .contact__card {
    position: absolute; left: 30px; top: 646px; width: 310px;
    text-align: center; color: #fff; font-style: normal;
  }
  .contact__name {
    color: var(--lime-light); font-weight: 700; font-size: 14px;
    letter-spacing: .5px; line-height: 1.35; text-transform: uppercase;
  }
  .contact__lines { margin-top: 8px; font-weight: 700; font-size: 15px; line-height: 1.45; }

  /* Cover panel */
  .brand--cover {
    position: absolute; left: 40px; top: 44px; width: 300px;
    font-size: 20px; line-height: 1.2; text-transform: uppercase;
  }
  .brand--cover .brand__dot { width: 48px; height: 48px; }
  .cover__photo {
    position: absolute; left: 0; top: 150px; width: 370px; height: 530px;
    background: linear-gradient(160deg, #cfd9b0 0%, #a7b880 30%, #ead9c8 60%, #8b7356 100%);
  }
  .mission {
    position: absolute; left: 36px; top: 668px; width: 300px; color: #fff;
  }
  .mission__title {
    color: var(--lime-light); font-size: 24px; font-weight: 700;
    text-align: center; margin-bottom: 8px;
  }
  .mission__text { font-size: 14px; font-weight: 700; line-height: 1.4; text-align: justify; }
</style>
</head>
<body>
  <div class="brochure">
    <div class="panel panel--cover">
      <div class="cover__photo" role="img" aria-label="Photo of a nurse with a stethoscope caring for a smiling senior woman holding a cane outdoors"></div>
    </div>

    <svg class="wave" viewBox="0 0 1110 858" aria-hidden="true">
      <path d="M0 585 C120 520 250 520 370 580 C500 640 620 640 740 630 C860 620 980 615 1110 660 L1110 858 L0 858 Z" fill="var(--lime)"/>
      <path d="M0 595 C120 532 250 532 370 592 C500 652 620 652 740 642 C860 632 980 627 1110 672 L1110 858 L0 858 Z" fill="var(--green)"/>
    </svg>

    <div class="fold" style="left:370px"></div>
    <div class="fold" style="left:740px"></div>

    <section class="panel panel--about">
      <h2 class="about__title">What is<br>Home Health Care?</h2>
      <div class="about__body">
        <p><strong>Home health care</strong> provides skilled nursing care, physical therapy, occupational therapy, speech therapy, and medical social services delivered in the comfort of your own home. This care may be provided for an injury, illness, or after a surgical procedure, with the goal of helping you recover, regain your independence and empowering you to reach and keep your best physical, mental, and social well-being.</p>
        <p><strong>Home health care is ordered by your doctor.</strong> Our home health care professionals work with you and your doctor to evaluate your health care needs and establish a plan of care to provide services to meet those needs. Home health care is usually less expensive, more convenient, and having care provided at home is most often preferred.</p>
      </div>
      <div class="about__photo" role="img" aria-label="Photo of a caregiver's hands holding an elderly person's hand"></div>
      <p class="quote"><span class="quote__mark">“</span> Your Health is Our Primary Concern <span class="quote__mark">”</span></p>
    </section>

    <section class="panel panel--contact">
      <div class="contact__photo" role="img" aria-label="Photo of two senior men laughing together in a living room"></div>
      <p class="notice">In compliance with Title VI of the Civil Rights Act of 1964, with Section 504 of the Rehabilitation Act of 1973 and with the Age Discrimination Act of 1975, Maple Crest Home Health Care of San Diego does not discriminate on the basis of race, color, gender, national origin, age or disability with regard to admission, access to treatment or employment. We will make every effort to comply with these and similar statutes.</p>
      <div class="brand brand--small"><span class="brand__dot"></span><span>Maple Crest</span></div>
      <address class="contact__card">
        <p class="contact__name">Maple Crest<br>Home Health Care of San Diego, Inc.</p>
        <p class="contact__lines">4827 Harbor Glen Road, Suite 3K<br>Encinitas, CA 92031<br>760-418-MAPL (office)<br>76- 529-MAPL (fax)<br>760-284-5536 (cell)</p>
      </address>
    </section>

    <section class="panel panel--cover">
      <div class="brand brand--cover"><span class="brand__dot"></span><span>Maple Crest<br>Home Health Care<br>of San Diego</span></div>
      <div class="mission">
        <h2 class="mission__title">Our Mission</h2>
        <p class="mission__text">Our mission is to provide high quality, multi-disciplinary care by competent, caring and well-trained professionals who are responsive to the needs of our patients, their families and the communities we serve.</p>
      </div>
    </section>
  </div>
</body>
</html>
```